New Print Material Needed for Renovation Company

We are looking to update our current Print Material to reflect the current process we offer to our clients. A lot of the information is also outdated along with many of the photos that are currently being used. We are a renovation company that specializes in residential and commercial renovations and custom builds.This project is MULTIPLE pages. We will pay the chosen designer an extra fee for the designing 3-4 additional pages that are similar to the chosen design. Attached is our current Print Material. We are hoping to update the look of them and some of the messaging. Our current company colors are white, blue and light grey and it will remain that way.

Industry/Entity Type

Construction Company

Font styles to use
Sans Serif

Colors
3176b5
ffffff

Requirements
Must have
• Easy to explain the process
• Easy to read and understand let alone
• Easy to navigate
Nice to have
• As much creativity as possible
Should not have
• no confusing text
• no confusing layout

```html
<!DOCTYPE html>
<html lang="en">
<head>
<meta charset="UTF-8">
<title>Master Builder Timeline</title>
<link href="https://fonts.googleapis.com/css2?family=Roboto:wght@300;400;500;700;900&display=swap" rel="stylesheet">
<style>
  :root {
    --brand-blue: #1f5f9e;
    --accent-blue: #3176b5;
    --ink: #1a1a1a;
    --panel: #e6e7e8;
    --paper: #ffffff;
  }
  * { box-sizing: border-box; margin: 0; padding: 0; }
  html, body { width: 1200px; height: 1200px; overflow: hidden; background: var(--paper); }
  body { font-family: 'Roboto', Arial, sans-serif; color: var(--ink); position: relative; }

  .sheet {
    position: absolute; left: 32px; top: 162px; width: 1134px; height: 876px;
    background: radial-gradient(ellipse at 55% 30%, #f6f6f7 0%, var(--panel) 70%);
  }
  .art { position: absolute; left: 0; top: 0; width: 1200px; height: 1200px; }
  .stage-circle { fill: var(--paper); filter: url(#lift); }
  .stage-arc { fill: none; stroke: var(--brand-blue); stroke-linecap: round; }

  .title { position: absolute; left: 234px; top: 214px; color: var(--brand-blue); line-height: 0.86; }
  .title span { display: block; font-size: 55px; letter-spacing: 3px; }
  .title .strong { font-weight: 900; }
  .title .light { font-weight: 300; }

  .step-tag {
    position: absolute; height: 38px; border: 1.5px solid var(--brand-blue);
    background: transparent; font-size: 31px; line-height: 35px; text-align: center;
    letter-spacing: 1.5px; color: var(--ink);
  }
  .step-tag b { font-weight: 700; }
  .step-tag span { font-weight: 300; }

  .stage-text { position: absolute; text-align: center; transform: translateX(-50%); }
  .phase { margin-bottom: 21px; }
  .phase h3 { font-size: 18px; font-weight: 500; color: var(--brand-blue); line-height: 21px; letter-spacing: 0.2px; }
  .phase .duration { font-size: 17px; font-weight: 500; color: var(--brand-blue); line-height: 20px; letter-spacing: 0.5px; }
  .phase p { font-size: 15px; line-height: 19px; color: var(--ink); }
  .start-date { font-size: 18px; font-weight: 500; color: var(--brand-blue); }

  .company-block {
    position: absolute; left: 899px; top: 866px; width: 214px; height: 118px;
    background: var(--brand-blue); display: flex; align-items: center; justify-content: center; gap: 12px;
  }
  .company-block .dot { width: 28px; height: 28px; border-radius: 50%; background: var(--paper); flex: none; }
  .company-block .name { color: var(--paper); font-size: 15px; font-weight: 400; line-height: 18px; }
</style>
</head>
<body>
  <div class="sheet"></div>

  <svg class="art" viewBox="0 0 1200 1200" xmlns="http://www.w3.org/2000/svg">
    <defs>
      <filter id="lift" x="-20%" y="-20%" width="140%" height="140%">
        <feDropShadow dx="4" dy="8" stdDeviation="9" flood-color="#000" flood-opacity="0.22"/>
      </filter>
    </defs>
    <circle class="badge" cx="152" cy="282" r="68" fill="#1f5f9e" role="img" aria-label="Serrated badge with crossed wrench and screwdriver tool icon"/>

    <circle class="stage-circle" cx="280" cy="578" r="206"/>
    <path class="stage-arc" stroke-width="5" d="M75 560 A206 206 0 1 1 477 638"/>

    <circle class="stage-circle" cx="896" cy="445" r="210"/>
    <path class="stage-arc" stroke-width="5" d="M896 235 A210 210 0 0 0 776 617"/>

    <circle class="stage-circle" cx="646" cy="787" r="214"/>
    <path class="stage-arc" stroke-width="9" d="M435 824 A214 214 0 1 1 859 806"/>
  </svg>

  <div class="title">
    <span class="strong">MASTER</span>
    <span class="light">BUILDER</span>
    <span class="light">TIMELINE</span>
  </div>

  <div class="step-tag" style="left:558px; top:213px; width:233px;"><b>STEP3:</b><span>BUILD</span></div>
  <div class="step-tag" style="left:878px; top:736px; width:215px;"><b>STEP2:</b><span>PLAN</span></div>
  <div class="step-tag" style="left:136px; top:809px; width:254px;"><b>STEP1:</b><span>DESIGN</span></div>

  <section class="stage-text" style="left:272px; top:392px; width:380px;">
    <div class="phase">
      <h3>INITIAL<br>DESIGN MEETING</h3>
      <div class="duration">1—2 weeks</div>
      <p>The first step of the design process is to<br>confirm the design concept you have<br>envisioned.</p>
    </div>
    <div class="phase">
      <h3>SECOND DESIGN MEETING</h3>
      <div class="duration">1—2 weeks</div>
      <p>Our designers work directly with you to ensure the<br>measurements line up with your design ideas.</p>
    </div>
    <div class="phase">
      <h3>FINAL DESIGN MEETING</h3>
      <div class="duration">Plan &amp; Scope: 1—3 weeks</div>
      <p>Any last minute or final revisions<br>will be completed within<br>three days of this<br>meeting.</p>
    </div>
  </section>

  <section class="stage-text" style="left:901px; top:284px; width:380px;">
    <div class="phase">
      <h3>MATERIAL FINALIZATION</h3>
      <div class="duration">2—4 weeks</div>
      <p>A lead designer will finalize any revisions you<br>may have for your material selection.</p>
    </div>
    <div class="phase">
      <h3>FINAL DOC. + CONSTRUCTION PLANS</h3>
      <div class="duration">2—6 weeks</div>
      <p>The drawings will be updated with 24 hours once the<br>permits have been approved and received.</p>
    </div>
    <div class="phase">
      <h3>SCHEDULING</h3>
      <div class="duration">2—4 weeks</div>
      <p>All designs, dates, permits have been complet-<br>ed. The project is read to get underway.</p>
    </div>
    <div class="start-date">START DATE: TBA</div>
  </section>

  <section class="stage-text" style="left:649px; top:642px; width:380px;">
    <div class="phase">
      <h3>MATERIAL SELECTION</h3>
      <div class="duration">1—4 weeks</div>
      <p>Our material selection coordinator will<br>work with you to ensure all the right<br>materials.</p>
    </div>
    <div class="phase">
      <h3>ENGINEERING DRAWINGS</h3>
      <div class="duration">2—4 weeks</div>
      <p>The final permit drawings will be sent to engineers<br>to ensure structural integrity.</p>
    </div>
    <div class="phase">
      <h3>COMPLETE BUILDING PERMIT PLANS</h3>
      <div class="duration">3—25 weeks</div>
      <p>Permit drawings will begin once the<br>build has signed and initial<br>payments have been<br>made.</p>
    </div>
  </section>

  <div class="company-block">
    <div class="dot"></div>
    <div class="name">Harbourline<br>General<br>Contractors</div>
  </div>
</body>
</html>
```